Tamberlin & Co Boutique Accommodation & Open Garden

Boutique Accommodation & Open garden; Weddings, Functions & Tours
A 1904 cottage is surrounded by 5 acres of landscaped gardens 3 of which are open to the public.
The many pathways entice it’s visitor to wonder under romantic rose covered arbours leading them to secluded flower filled areas.
The woodlands create a shady haven to rest in, while the pond at the bottom of the garden adds to the peace and tranquility felt by all in this harmonies spellbinding garden.

Open Thursday through Sunday, or by appointment.

I would like to down load my Logo. How do I do this?

Target Market(s)

Affluent

Colors

Designer to choose colors to be used in the design.

Requirements
Must have
• The Logo, Simplistic and classy.
• I am a graphic designer so have high expectations, but no time to do it myself. The design must be good.What to see and when.
Nice to have
• I am after a great design, must be classy must stand out. Not the run of the mill that everyone has.
Should not have
• Colours must complement Logo. Colours as in the saltwater @ narooma and black background with white writing.

```html
<!DOCTYPE html>
<html lang="en">
<head>
<meta charset="utf-8">
<title>Tamberlin &amp; Co — Brochure</title>
<link rel="stylesheet" href="https://fonts.googleapis.com/css2?family=Cormorant+Garamond:ital,wght@0,400;0,500;0,600;1,400;1,600&family=Raleway:wght@300;400&display=swap">
<style>
:root{
  --stage:#ffffff;
  --ink:#0c0c0c;
  --paper:#f4f4f2;
  --rule:#d8d8d8;
}
*{margin:0;padding:0;box-sizing:border-box}
html,body{width:1200px;height:1000px;overflow:hidden;background:var(--stage)}
body{position:relative;font-family:"Cormorant Garamond",Georgia,serif;color:var(--paper)}
.spread{position:absolute;left:262px;width:675px;height:477px;background:var(--ink);overflow:hidden;box-shadow:0 3px 8px rgba(0,0,0,.25)}
.spread--outside{top:10px}
.spread--inside{top:509px}
.photo{position:absolute}
.green-a{background:linear-gradient(160deg,#6f8f4e,#2e4c22 55%,#17260f)}
.green-b{background:linear-gradient(200deg,#8fae6a,#3d6030 60%,#1d2f14)}
.green-c{background:linear-gradient(135deg,#4a6b35,#9bb47a 50%,#2f4a22)}
.cottage{background:linear-gradient(170deg,#7a6a6a,#8e9b7a 45%,#3e5a2a)}
.interior{background:linear-gradient(150deg,#cfd2d6,#8d8f96 55%,#5b5450)}
.flowers{background:linear-gradient(140deg,#2d4a22,#7a2d36 50%,#3c5d2c)}
.pink-tree{background:linear-gradient(160deg,#c9738a,#5d7a3e 60%,#24381a)}
.white-bloom{background:linear-gradient(150deg,#e4e8e0,#8caa78 55%,#2d4724)}

/* outside spread */
.cover-panel{position:absolute;left:0;top:0;width:224px;height:477px}
.cover-panel .photo{left:0;top:0;width:224px;height:320px;background:linear-gradient(180deg,#5c7a3e 0%,#3c5d2a 45%,#1d3014 75%,var(--ink) 100%)}
.cover-frame{position:absolute;left:10px;top:10px;width:204px;height:457px;border:1px solid var(--paper)}
.cover-text{position:absolute;left:18px;top:324px;width:188px;font-size:8.8px;line-height:1.32;text-align:center}
.cover-text p{margin-bottom:9px}
.cover-text em{font-weight:600}

.contact{position:absolute;left:224px;top:0;width:228px;height:240px;text-align:center}
.contact h2{font-family:"Raleway",Arial,sans-serif;font-weight:400;font-size:14px;letter-spacing:.5px;margin-top:25px}
.contact .rule{width:140px;height:1px;background:var(--paper);margin:6px auto 9px}
.contact .intro{font-style:italic;font-size:9.5px;line-height:1.3;padding:0 16px}
.contact .intro p{margin-bottom:2px}
.contact-lines{list-style:none;font-size:9.5px;margin-top:11px}
.contact-lines li{display:flex;justify-content:center;align-items:center;gap:4px;margin-bottom:6px}
.contact-lines .pair{gap:18px}
.contact-lines span{display:inline-flex;align-items:center;gap:4px}
.contact-lines svg{width:8px;height:8px;fill:var(--paper)}
.address{font-size:10.5px;line-height:1.3;margin-top:12px}

.name-panel{position:absolute;left:457px;top:250px;width:218px;height:122px;background:var(--ink);display:flex;align-items:center;justify-content:center}
.name-panel .brand-name{font-size:22px;font-weight:500;line-height:1}

/* inside spread */
.season-panel{position:absolute;left:0;top:0;width:452px;height:477px}
.season-title{font-family:"Raleway",Arial,sans-serif;font-weight:400;font-size:13.5px;text-align:center;margin-top:20px;letter-spacing:.3px}
.season-title::after{content:"";display:block;width:180px;height:1px;background:var(--paper);margin:5px auto 0}
.season-table{position:absolute;left:18px;top:57px;width:420px;border-collapse:collapse;font-size:8.3px;line-height:1.2}
.season-table th{background:var(--paper);color:var(--ink);font-weight:600;font-size:9.5px;height:22px;letter-spacing:.3px}
.season-table td{border:1px solid var(--rule);height:31px;padding:2px 5px;vertical-align:middle}
.season-table td.month{text-align:center;font-weight:600;width:57px}
.season-table td:nth-child(2){width:182px}
</style>
</head>
<body>

<section class="spread spread--outside">
  <div class="cover-panel">
    <div class="photo" role="img" aria-label="Photo of the 1904 cottage above a lawn with red flower beds"></div>
    <div class="cover-frame"></div>
    <div class="cover-text">
      <p>This <em>1904 cottage</em> is surrounded by 5 acres of landscaped gardens 3 of which are open to the public.</p>
      <p>The many pathways entice it's visitor to wonder under romantic rose covered arbours leading them to secluded flower filled areas.</p>
      <p>The woodlands create a shady haven to rest in, while the pond at the bottom of the garden adds to the peace and tranquility felt by all in this harmonies spellbinding garden.</p>
    </div>
  </div>

  <div class="contact">
    <h2>CONTACT US</h2>
    <div class="rule"></div>
    <div class="intro">
      <p>Feel free to call us or contact us via email.</p>
      <p>We welcome any comments, questions or suggestions you may have that will allow us to serve you better.</p>
    </div>
    <ul class="contact-lines">
      <li class="pair">
        <span><svg viewBox="0 0 10 10"><path d="M2 0.5l2 2-1 1.3c.6 1.3 1.6 2.3 2.9 2.9L7.2 5.6l2.3 2-1.2 1.9C4.5 9.5.6 5.5.5 1.7z"/></svg>02 4400 1928</span>
        <span><svg viewBox="0 0 10 10"><rect x="2.5" y="0.5" width="5" height="9" rx="1"/></svg>0400 512 377</span>
      </li>
      <li><svg viewBox="0 0 10 10"><path d="M0 2h10v6H0zM0 2l5 3.5L10 2" stroke="#0c0c0c" stroke-width=".8"/></svg>info@tamberlingardens.au</li>
      <li><svg viewBox="0 0 10 10"><circle cx="5" cy="5" r="4.5"/></svg>www.tamberlingardens.au</li>
    </ul>
    <div class="address">
      Tamberlin &amp; Co Open Garden<br>
      148 Wattle Ridge Road,<br>
      Bellbird Creek, NSW 2550
    </div>
  </div>

  <div class="photo green-b" style="left:226px;top:242px;width:109px;height:68px" role="img" aria-label="Photo of clipped hedge garden with a central urn"></div>
  <div class="photo cottage" style="left:337px;top:242px;width:115px;height:148px" role="img" aria-label="Photo of gabled cottages with potted plants along a gravel path"></div>
  <div class="photo green-a" style="left:226px;top:312px;width:109px;height:78px" role="img" aria-label="Photo of a house framed by trees and lawn"></div>
  <div class="photo interior" style="left:226px;top:392px;width:144px;height:85px" role="img" aria-label="Photo of a cosy bedroom in the accommodation"></div>
  <div class="photo green-c" style="left:372px;top:392px;width:80px;height:85px" role="img" aria-label="Photo of a stone lantern among greenery"></div>

  <div class="photo" style="left:457px;top:0;width:218px;height:246px;background:linear-gradient(180deg,#7a6a52,#5a6a3e 45%,#3c5a2a 80%,#6b4f36)" role="img" aria-label="Photo of an arched pear tree tunnel over a leafy path"></div>

  <div class="name-panel">
    <span class="brand-name">Tamberlin &amp; Co</span>
  </div>

  <div class="photo flowers" style="left:457px;top:375px;width:218px;height:102px" role="img" aria-label="Photo of a verandah with chairs and red geraniums"></div>
</section>

<section class="spread spread--inside">
  <div class="season-panel">
    <h2 class="season-title">WHAT TO SEE AND WHEN</h2>
    <table class="season-table">
      <thead><tr><th>MONTH</th><th>FIRST FORTNIGHT</th><th>LAST FORTNIGHT</th></tr></thead>
      <tbody>
        <tr><td class="month">September</td><td>For-get-me-nots, Violets, Magnolias, Arum Lillies, Freesias, Camelias, Wisteria, Pear Arbour</td><td>Azaleas, Bluebells, McCartney Rose, Early Blossom, Bulbs, Freesias, Forget-me-nots</td></tr>
        <tr><td class="month">October</td><td>Crabapples, lots of Spring flowers in blossom, Wisteria, Poppies, Citrus, Spring Annuals</td><td>Early Roses, Iris, Water Iris, Foxgloves, Cherry Blossom, Lilacs, Snowbells, Crabapples</td></tr>
        <tr><td class="month">November</td><td>Crabapples, Water Iris, Roses Abundant, Foxgloves, Elderberry Hedge with Wild Roses</td><td>Roses, Flower Borders, Lavenders, Delphiniums, Hawthorns</td></tr>
        <tr><td class="month">December</td><td>Roses, Buddleia, Flower Borders, Delphiniums</td><td>Roses Buddleia, Flower Borders, Lavenders, Hydrangeas</td></tr>
        <tr><td class="month">January</td><td>Roses, Dahlias, Flower Borders, Hydrangeas, Veggy Patch</td><td>Lilium Bulbs, Flower Borders, Dashlias, Roses Hydrangeas</td></tr>
        <tr><td class="month">February</td><td>Salvias, Flower Borders, Dahlias, Kitchen Garden, Apples, Pears</td><td>Early Easter Daisy, Flower Borders, Autumn Roses, Dahlias</td></tr>
        <tr><td class="month">March</td><td>Plectranthus, Belladonna Lillies, Buddleias, Salvias, Dahlias, Autumn Roses</td><td>Fruit Ripening on Apples and Pears, Autumn Roses, Easter Daisy, Salvias, Flower Borders</td></tr>
        <tr><td class="month">April</td><td>Early Sasanqua Camelias, Flower Borders, Early Autumn Tones</td><td>Flower Borders, Early Autumn Colour, Jackhumm, Crabapples</td></tr>
        <tr><td class="month">May</td><td>Chrysanthemums, Autum colour, Mexican Sage</td><td>Sasanqua Camelias, Autumn Leaf Colour, Mexican Sage</td></tr>
        <tr><td class="month">June</td><td>Late Autumn Colour, Early Jonquils, Citrus</td><td>Bare Pear Arbour</td></tr>
        <tr><td class="month">July</td><td>Bare Winter Look, Bulbs, Magnolias</td><td>Very Wintery, Jonquils, Magnolias, Camelias</td></tr>
        <tr><td class="month">August</td><td>Daphne, Japonica Hedge, Magnolias, Bulbs Camelias, Helleborus</td><td>Magnolias, Early Plum Blossom</td></tr>
      </tbody>
    </table>
  </div>

  <div class="photo cottage" style="left:452px;top:0;width:223px;height:95px" role="img" aria-label="Photo of the cottage front with blue flowers and potted topiary"></div>
  <div class="photo interior" style="left:452px;top:97px;width:109px;height:98px" role="img" aria-label="Photo of a bright sitting room with flowers"></div>
  <div class="photo green-b" style="left:563px;top:97px;width:112px;height:65px" role="img" aria-label="Photo of clipped shrubs in a garden bed"></div>
  <div class="photo pink-tree" style="left:563px;top:164px;width:112px;height:118px" role="img" aria-label="Photo of a pink flowering tree above hedges"></div>
  <div class="photo green-a" style="left:452px;top:197px;width:109px;height:85px" role="img" aria-label="Photo of a winding garden path under trees"></div>
  <div class="photo green-c" style="left:452px;top:284px;width:80px;height:100px" role="img" aria-label="Photo of a green lawn bordered by shrubs"></div>
  <div class="photo green-b" style="left:534px;top:284px;width:141px;height:100px" role="img" aria-label="Photo of the garden path leading to the cottage"></div>
  <div class="photo green-a" style="left:452px;top:386px;width:131px;height:91px" role="img" aria-label="Photo of a garden gazebo surrounded by flowers"></div>
  <div class="photo white-bloom" style="left:585px;top:386px;width:90px;height:91px" role="img" aria-label="Photo of white flower blossoms"></div>
</section>

</body>
</html>
```